Business Card Design - Pediatric Dentist

We need a business card for a new dental office. We are a pediatric dentist in Austin Tx. I would like a design that use bright green and if possible light blue.

Target Market(s)

Marketed to young moms

Industry/Entity Type

Dental

Contact Information for Business Card

Marcus Hollin DDS
Tidewell Pediatric Dentistry
438 E. Corvell Lane. Austin TX 78731
(512) 284 9153.

In the back i would like to state "we take most insurances, Chip & Medicaid" & a map

Colors
add136
cadf82
85cae6

```html
<!DOCTYPE html>
<html lang="en">
<head>
<meta charset="utf-8">
<title>Tidewell Pediatric Dentistry – Card Back</title>
<link rel="stylesheet" href="https://fonts.googleapis.com/css2?family=Comfortaa:wght@400&display=swap">
<style>
  :root {
    --paper: #ffffff;
    --lime: #9eff00;
    --sky: #7fd9dc;
    --ink: #111111;
    --map-base: #e9e7e1;
    --tooth-light: #f4f6f2;
    --tooth-shade: #7d8a70;
  }
  html, body {
    margin: 0;
    padding: 0;
    width: 1200px;
    height: 704px;
    overflow: hidden;
    background: var(--paper);
  }
  .card-back {
    position: relative;
    width: 1200px;
    height: 704px;
    overflow: hidden;
    background: var(--paper);
  }
  .card-back svg {
    position: absolute;
    inset: 0;
    display: block;
  }
  .lime-field { fill: var(--lime); }
  .sky-band { fill: var(--sky); }
  .insurance-line {
    font-family: "Comfortaa", sans-serif;
    font-size: 29px;
    fill: var(--ink);
    letter-spacing: 0.2px;
  }
  .map-frame { fill: var(--map-base); }
  .address-line {
    font-family: "Comfortaa", sans-serif;
    font-size: 19px;
    fill: var(--ink);
    letter-spacing: 1px;
  }
</style>
</head>
<body>
<main class="card-back">
  <svg viewBox="0 0 1200 704" width="1200" height="704" xmlns="http://www.w3.org/2000/svg">
    <defs>
      <linearGradient id="tooth-tone" x1="0" y1="0" x2="1" y2="0">
        <stop offset="0" stop-color="var(--tooth-shade)" stop-opacity="0.35"/>
        <stop offset="0.55" stop-color="var(--tooth-light)" stop-opacity="0.25"/>
        <stop offset="1" stop-color="var(--tooth-shade)" stop-opacity="0.3"/>
      </linearGradient>
      <filter id="map-shadow" x="-10%" y="-10%" width="130%" height="130%">
        <feDropShadow dx="4" dy="5" stdDeviation="3" flood-color="#000" flood-opacity="0.45"/>
      </filter>
    </defs>

    <path class="lime-field" d="M0 0 H662 A503 503 0 0 1 662 704 H0 Z"/>

    <rect class="tooth-art" x="378" y="0" width="576" height="704" rx="120"
          fill="url(#tooth-tone)" role="img"
          aria-label="Large glossy molar tooth illustration, half green and half white"/>

    <text class="insurance-line" x="647" y="280" text-anchor="middle">"we take most insurances, Chip &amp; Medicaid"</text>

    <rect class="sky-band" x="0" y="301" width="1200" height="27"/>
    <rect class="sky-band" x="0" y="355" width="1200" height="23"/>

    <g transform="translate(976 488) rotate(-29)">
      <rect class="map-frame" x="-142" y="-98" width="284" height="196"
            filter="url(#map-shadow)" role="img"
            aria-label="Street map showing the office location near the highway"/>
    </g>

    <g transform="translate(940 650) rotate(-29)">
      <text class="address-line" x="0" y="0">438 E. Corvell Lane.</text>
      <text class="address-line" x="30" y="26">Austin TX 78731</text>
    </g>
  </svg>
</main>
</body>
</html>
```